Insert sheet for our Dog Food Package

We need an information sheet to go inn our pet food package, with branding, and information on ingredients, nutrition and feeding guidance. We will also need two additional items which will be a variation on the label design:
1) Label for package (detailed label about us and our food)
2) Label for outer shipping box (simple label for branding)
We will start with the information, insert page. The winning designer will then deliver the package and box labels as simplified versions of the same graphical theme.
I have attached samples of an earlier drafts of the insert piece. Please disregard the style, form and colors of the examples given. THEY ARE ONLY THERE TO SHOW WHAT INFORMATION SHOULD BE INCLUDED. All colors and style should be from our logo (attached). All graphics, font styles, and placement of elements need to be YOUR creative design - not a copy of the sample we gave. PLEASE READ THIS AND PLEASE DO NOT SUBMIT ANY VARIATION OF THE EXAMPLES!!!!!!!

Target Market(s)

Pet Owners

Industry/Entity Type

Pet Food

Colors
EB3D1F
EC4F4E
F09395
F8D3D4
FCEDEE

Requirements
Must have
• All new design. New colors (based in the palette of our logo), new graphics, new fonts, new placement of elements.
Should not have
• Please disregard the style, form and colors of the examples given. THEY ARE ONLY THERE TO SHOW WHAT INFORMATION SHOULD BE INCLUDED.

```html
<!DOCTYPE html>
<html lang="en">
<head>
<meta charset="utf-8">
<title>Venna Dog – Insert Sheet</title>
<link rel="stylesheet" href="https://fonts.googleapis.com/css2?family=Patrick+Hand&family=Quicksand:wght@500;600&family=Roboto+Condensed:wght@400;700&display=swap">
<style>
  :root {
    --page-bg: #e7e2da;
    --cream: #fcf6ea;
    --red: #b3272b;
    --brown: #4b1b15;
    --ink: #3a1d17;
    --line: #e9d8cc;
    --dog-light: #f2c891;
    --dog-deep: #d99a5b;
  }
  * { box-sizing: border-box; margin: 0; padding: 0; }
  html, body { width: 1200px; height: 1200px; overflow: hidden; }
  body {
    background: var(--page-bg);
    font-family: "Patrick Hand", cursive;
    color: var(--ink);
  }
  .sheet {
    position: absolute;
    left: 190px; top: 40px;
    width: 820px; height: 1120px;
    background: var(--cream);
    box-shadow: 0 6px 24px rgba(0,0,0,.18);
  }
  .band-top, .band-bottom { position: absolute; left: 0; width: 100%; background: var(--red); }
  .band-top { top: 0; height: 18px; }
  .band-bottom { bottom: 0; height: 28px; }

  .title {
    position: absolute; top: 44px; left: 0; width: 100%;
    text-align: center; font-size: 44px; font-weight: 400;
    letter-spacing: 1px; color: var(--ink);
  }
  .lead {
    position: absolute; top: 112px; left: 42px; width: 530px;
    font-size: 23px; line-height: 1.35; color: var(--red);
  }
  .quote {
    position: absolute; top: 210px; left: 42px; width: 520px;
    font-size: 23px; line-height: 1.45; color: var(--ink);
  }
  .mascot {
    position: absolute; top: 118px; left: 560px; width: 250px; height: 350px;
    background: radial-gradient(ellipse at 55% 40%, var(--dog-light) 0%, var(--dog-deep) 75%);
    border-radius: 46% 40% 0 0;
  }

  .info-band {
    position: absolute; top: 460px; left: 0; width: 100%; height: 420px;
    background: var(--brown); color: var(--cream);
    border-top: 4px solid var(--red);
  }
  .panel {
    position: absolute;
    border: 2px dashed var(--line);
    border-radius: 12px;
    padding: 14px 18px;
  }
  .panel-ingredients { left: 40px; top: 22px; width: 320px; height: 252px; border-bottom-left-radius: 0; border-bottom-right-radius: 0; }
  .panel-nutrition { left: 40px; top: 272px; width: 320px; height: 112px; border-top-left-radius: 0; border-top-right-radius: 0; }
  .panel-feeding { left: 358px; top: 22px; width: 424px; height: 362px; }

  .panel-kicker { font-size: 21px; margin-bottom: 4px; }
  .panel-heading { font-family: "Quicksand", sans-serif; font-weight: 600; font-size: 19px; margin-bottom: 10px; }
  .ingredient-list { font-family: "Quicksand", sans-serif; font-size: 12px; line-height: 1.45; }
  .nutrition-grid {
    display: grid; grid-template-columns: 1fr 1fr; gap: 2px 10px;
    font-family: "Quicksand", sans-serif; font-size: 12px;
  }
  .nutrition-grid span:nth-child(even) { text-align: right; }

  .feeding-table {
    width: 360px; border-collapse: collapse;
    font-family: "Quicksand", sans-serif; font-size: 15px;
  }
  .feeding-table th { font-weight: 500; text-align: left; padding: 0 8px 8px 0; }
  .feeding-table th:last-child { text-align: right; padding-right: 14px; }
  .feeding-table tbody { border: 1.5px solid var(--line); }
  .feeding-table td { padding: 4px 10px; }
  .feeding-table td:last-child { text-align: right; padding-right: 14px; }

  .brand-block {
    position: absolute; top: 918px; left: 262px;
    display: flex; align-items: center; gap: 22px;
  }
  .brand-mark {
    width: 120px; height: 120px; border-radius: 50%;
    background: var(--red);
  }
  .contact { font-family: "Roboto Condensed", sans-serif; font-size: 21px; line-height: 1.35; color: var(--ink); }
  .contact .brand-name, .contact .email { color: var(--red); font-weight: 700; }
  .contact .email { font-weight: 400; }
</style>
</head>
<body>
  <main class="sheet">
    <div class="band-top"></div>

    <h1 class="title">PREPARED WITH LOVE FOR SHADOW</h1>
    <p class="lead">We Revolutionizes the industry. Not Formulated to meet a minimun standard, but to develop the maximum health of the whole dog.</p>
    <p class="quote">" We didn't just set about to create a food that will pass a minimum standard'. We set out to revolutionize the industry by creating a food that is designed with Superfoods, Wholesoe Grains, and Powerful Oils to help your dog achieve their maximu health, happiness and longevity'.</p>
    <div class="mascot" role="img" aria-label="Illustration of a happy golden spaniel wearing a red bandana"></div>

    <section class="info-band">
      <div class="panel panel-ingredients">
        <p class="panel-kicker">We Prepared the best for shadow</p>
        <h2 class="panel-heading">Ingredients:</h2>
        <p class="ingredient-list">Potassium Citrate, DiCalcium Phosphate, Calcium Carbonate, Garbanzo Beans, Choline Bitartrate, Taurine, Salt, Zinc Proteinate, Magnesium Oxide, Iron Proteinate, Vitamin B-12, Selenium, Niacin, Riboflavin, Calcium Panthothenate, Thiamine, Vitamin A, Vitamin D, Calcium Iodate, Vitamin B6, Folic Acid</p>
      </div>
      <div class="panel panel-nutrition">
        <h2 class="panel-heading">Nutritional Information:</h2>
        <div class="nutrition-grid">
          <span>Protein: 15%</span><span>Total Fat: 9.5%</span>
          <span>Moisture: 72%</span><span>Crude Fiber: 2.0%</span>
        </div>
      </div>
      <div class="panel panel-feeding">
        <p class="panel-kicker">How much should I feed Shadow?</p>
        <h2 class="panel-heading">Recommended Feeding Plan:</h2>
        <table class="feeding-table">
          <thead><tr><th>Approximate Weight</th><th>Full Meal</th></tr></thead>
          <tbody><tr><td>&lt;20 lbs</td><td>110 g</td></tr></tbody>
          <tbody>
            <tr><td>20-29 lbs</td><td>200 g</td></tr>
            <tr><td>30-39 lbs</td><td>250 g</td></tr>
            <tr><td>40-54 lbs</td><td>300 g</td></tr>
          </tbody>
          <tbody>
            <tr><td>55-69 lbs</td><td>350 g</td></tr>
            <tr><td>70-85 lbs</td><td>400 g</td></tr>
          </tbody>
          <tbody><tr><td>85+ lbs</td><td>500 g</td></tr></tbody>
        </table>
      </div>
    </section>

    <footer class="brand-block">
      <div class="brand-mark"></div>
      <address class="contact" style="font-style:normal">
        <div class="brand-name">Venna Dog™</div>
        <div>118 Orchard Ln.</div>
        <div>Fairmont, NY</div>
        <div class="email">info@vennadog.com</div>
      </address>
    </footer>

    <div class="band-bottom"></div>
  </main>
</body>
</html>
```